Corbel Path Advisory WordPress Design

Corbel Path Advisory is a consulting company that targets small business. We use our genius in the field to help small Business navigate information systems, in particular Tallybridge Solutions.

We are looking for a WordPress Design that is playful but intelligent for our web site. The design should plays off of our Corbel Logo and be informative. The attachments is of our logo variations that will be used in your design. It should be useful to describe the look and feel of the site we are looking to get.

The color of the website is not defined yet but should work well with our logo colors.

Regarding to the template and the way to display the home page. The menu should contain the following items which will each be its own page:
1. Home Page
2. Blog
-This needs to be a frame work to allow us to constantly add written articles and Video logs with Transcripts possibly in two sections.
3. What Corbel Does
-This will contain the company approach
4. Request a Corbel
-This will be a form to collect contact information
5. Contact Corbel
6. About Us

Please keep the SIMILAR airy/mythical design used in the logo.

Finally, we need a design that will have a normal view and a mobile view.

Target Market(s)

Corbel Path Advisory is a consulting company that targets small business.

Industry/Entity Type

Business Consultant

Requirements
Must have
• Regarding to the template and the way to display the home page. The menu should contain the following items which will each be its own page:
• 1. Home Page
• 2. Blog
• -This needs to be a frame work to allow us to constantly add written articles and Video logs with Transcripts possibly in two sections.
• 3. What Corbel Does
• -This will contain the company approach
• 4. Request a Corbel
• -This will be a form to collect contact information
• 5. Contact Corbel
• 6. About Us
• Mobile View
Nice to have
• Have a magical or mythical quality like the hands around the logo but not to playful.
Should not have
• Our slogan is "Corbel solutions that make business work!"

```html
<!DOCTYPE html>
<html lang="en">
<head>
<meta charset="utf-8">
<title>Corbel Path Advisory</title>
<link rel="stylesheet" href="https://fonts.googleapis.com/css2?family=Open+Sans:wght@400;600;700&family=Raleway:wght@500;600;700&display=swap">
<style>
:root{
  --blue:#2f63b4;
  --blue-dark:#1f4a92;
  --blue-light:#4f86d6;
  --orange:#f5a31a;
  --text:#6b6f75;
  --head:#2f5fab;
  --gray-band:#eceef1;
  --line:#dfe2e6;
  --white:#ffffff;
}
*{box-sizing:border-box;margin:0;padding:0}
html,body{width:896px;height:1200px;overflow:hidden;background:var(--white)}
body{font-family:"Open Sans",Arial,sans-serif;color:var(--text);position:relative}
.container{width:560px;margin:0 auto;position:relative}

.site-header{height:90px}
.brand{display:flex;align-items:center;gap:10px;position:absolute;left:0;top:22px}
.brand-mark{width:44px;height:44px;border-radius:50%;background:var(--orange)}
.brand-name{font-family:"Raleway",Arial,sans-serif;font-weight:700;font-size:21px;color:var(--blue)}

.main-nav{height:24px;background:linear-gradient(var(--blue-light),var(--blue))}
.main-nav ul{list-style:none;display:flex;height:24px;align-items:center}
.main-nav li{font-size:9.5px;font-weight:700;color:var(--white);padding:0 9px;border-right:1px solid rgba(255,255,255,.35);letter-spacing:.2px}
.main-nav li:first-child{padding-left:6px}
.main-nav li:last-child{border-right:none}

.hero{height:267px;position:relative;background:linear-gradient(100deg,#f4f7fb 0%,#dbe6f2 40%,#b8cbe0 70%,#8ea7c6 100%)}
.hero-photo{position:absolute;inset:0}
.hero-copy{position:absolute;top:150px;left:0;width:280px}
.hero-title{font-family:"Raleway",Arial,sans-serif;font-weight:700;font-size:21px;color:var(--head)}
.hero-sub{font-family:"Raleway",Arial,sans-serif;font-weight:600;font-size:15px;color:var(--head);margin-top:2px}
.hero-text{font-size:8px;line-height:11px;margin-top:6px;color:#4c5158}
.dots{display:flex;gap:6px;margin-top:10px}
.dots span{width:9px;height:9px;border-radius:50%;background:#3a3f47}
.dots span.active{background:var(--blue)}

.features{display:flex;margin-top:24px;height:195px}
.feature{flex:1;text-align:center;padding:12px 16px 0;border-right:1px solid var(--line)}
.feature:last-child{border-right:none}
.feature-icon{width:36px;height:36px;margin:0 auto}
.feature h3{font-family:"Raleway",Arial,sans-serif;font-weight:600;font-size:15px;color:var(--head);margin-top:14px}
.feature p{font-size:8px;line-height:11px;margin-top:6px}
.learn-more{display:block;font-size:8.5px;font-weight:700;color:var(--orange);margin-top:6px}

.approach{background:linear-gradient(var(--gray-band),#f6f7f9);height:240px;margin-top:15px}
.approach .container{height:240px}
.approach-copy{position:absolute;left:0;top:38px;width:350px}
.approach h2{font-family:"Raleway",Arial,sans-serif;font-weight:600;font-size:24px;color:var(--head)}
.approach p{font-size:8px;line-height:11px;margin-top:8px}
.btn{display:inline-block;font-size:7.5px;font-weight:700;color:var(--white);padding:5px 12px;border-radius:2px;margin-top:12px}
.btn-blue{background:var(--blue)}
.btn-orange{background:var(--orange)}
.approach-art{position:absolute;right:0;top:30px;width:190px;height:180px;border-radius:6px;background:radial-gradient(circle at 50% 55%,#cfe0f5 0%,#e7eef7 55%,rgba(236,238,241,0) 75%)}

.highlights{display:flex;gap:25px;margin-top:21px}
.highlight{flex:1}
.highlight-photo{height:102px;background:linear-gradient(135deg,#e9edf2,#b9c6d6 60%,#8f9fb5)}
.highlight h3{font-family:"Raleway",Arial,sans-serif;font-weight:600;font-size:15px;color:var(--head);margin-top:12px}
.highlight p{font-size:8px;line-height:11px;margin-top:5px}
.highlight .btn{margin-top:8px}

.site-footer{position:absolute;left:0;right:0;bottom:0;height:90px;background:linear-gradient(var(--blue-light),var(--blue-dark))}
.site-footer .container{height:90px}
.footer-nav{list-style:none;display:flex;position:absolute;left:0;top:26px}
.footer-nav li{font-size:8.5px;font-weight:700;color:var(--white);padding:0 6px;border-right:1px solid rgba(255,255,255,.5)}
.footer-nav li:first-child{padding-left:0}
.footer-nav li:last-child{border-right:none}
.copyright{position:absolute;left:0;top:46px;font-size:7.5px;color:#d5e2f5}
.social{position:absolute;right:0;top:24px;display:flex;gap:8px}
.social span{width:15px;height:15px;border-radius:50%;background:var(--white)}
</style>
</head>
<body>

<header class="site-header">
  <div class="container">
    <div class="brand">
      <span class="brand-mark"></span>
      <span class="brand-name">Corbel Path Advisory</span>
    </div>
  </div>
</header>

<nav class="main-nav">
  <div class="container">
    <ul>
      <li>HOME</li><li>BLOG</li><li>WHAT CORBEL DOES</li><li>REQUEST A CORBEL</li><li>CONTACT CORBEL</li><li>ABOUT US</li>
    </ul>
  </div>
</nav>

<section class="hero">
  <div class="hero-photo" role="img" aria-label="Business consultants meeting in a bright office"></div>
  <div class="container">
    <div class="hero-copy">
      <h1 class="hero-title">Small Business Consulting</h1>
      <p class="hero-sub">Eget fermentum lorem</p>
      <p class="hero-text">Clear advice on information systems for owners who want their tools and teams working together.</p>
      <div class="dots"><span class="active"></span><span></span><span></span><span></span></div>
    </div>
  </div>
</section>

<main class="container">
  <section class="features">
    <div class="feature">
      <svg class="feature-icon" viewBox="0 0 36 36" aria-hidden="true"><circle cx="18" cy="18" r="16" fill="none" stroke="#f5a31a" stroke-width="3"/><circle cx="18" cy="18" r="6" fill="#f5a31a"/></svg>
      <h3>Business Consulting</h3>
      <p>Practical guidance that helps small teams plan, choose and run the right systems.</p>
      <span class="learn-more">Learn More</span>
    </div>
    <div class="feature">
      <svg class="feature-icon" viewBox="0 0 36 36" aria-hidden="true"><circle cx="18" cy="18" r="17" fill="#f5a31a"/><path d="M13 14a5 5 0 1 1 7 4.5c-1.5.8-2 1.6-2 3.5" fill="none" stroke="#fff" stroke-width="3" stroke-linecap="round"/><circle cx="18" cy="27" r="2" fill="#fff"/></svg>
      <h3>Why Choose Us</h3>
      <p>Years of hands-on experience and a friendly approach that keeps things simple.</p>
      <span class="learn-more">Learn More</span>
    </div>
    <div class="feature">
      <svg class="feature-icon" viewBox="0 0 36 36" aria-hidden="true"><path d="M18 3a11 11 0 0 0-6 20v4h12v-4A11 11 0 0 0 18 3z" fill="#f5a31a"/><rect x="13" y="29" width="10" height="4" rx="1" fill="#f5a31a"/></svg>
      <h3>Business Ideas</h3>
      <p>Fresh ideas for growing your business with smarter processes and shared data.</p>
      <span class="learn-more">Learn More</span>
    </div>
  </section>
</main>

<section class="approach">
  <div class="container">
    <div class="approach-copy">
      <h2>What Corbel Does</h2>
      <p>We listen first, map how your business really works and then shape Tallybridge Solutions around your people rather than the other way round.</p>
      <p>From first setup to daily support, our consultants guide each step so your team gains confidence, saves time and keeps information in one trusted place.</p>
      <span class="btn btn-blue">READ MORE</span>
    </div>
    <div class="approach-art" role="img" aria-label="Illustration of a meditating figure surrounded by floating screens"></div>
  </div>
</section>

<section class="container highlights">
  <article class="highlight">
    <div class="highlight-photo" role="img" aria-label="Team working together at a desk"></div>
    <h3>About Us</h3>
    <p>A small team of advisors who help owners make technology work for their business.</p>
    <span class="btn btn-orange">READ MORE</span>
  </article>
  <article class="highlight">
    <div class="highlight-photo" role="img" aria-label="Consultant meeting with a client"></div>
    <h3>Request a Corbel</h3>
    <p>Tell us about your goals and we will arrange a short call to get started.</p>
    <span class="btn btn-orange">READ MORE</span>
  </article>
  <article class="highlight">
    <div class="highlight-photo" role="img" aria-label="Colleagues reviewing notes on a laptop"></div>
    <h3>Blog Post</h3>
    <p>Articles and video logs with transcripts on running a smarter small business.</p>
    <span class="btn btn-orange">READ MORE</span>
  </article>
</section>

<footer class="site-footer">
  <div class="container">
    <ul class="footer-nav">
      <li>HOME</li><li>BLOG</li><li>WHAT CORBEL DOES</li><li>REQUEST A CORBEL</li><li>CONTACT CORBEL</li><li>ABOUT US</li>
    </ul>
    <p class="copyright">© Corbel Path Advisory. All rights reserved.</p>
    <div class="social" aria-label="Social links"><span></span><span></span><span></span></div>
  </div>
</footer>

</body>
</html>
```